Print and eBook Cover Design for American Police Book

I need a book cover (front, spine, and back) designed for my completed book. The cover needs to be 5 x 8 and will be uploaded to Pellorin. The title is:

Steady Hands at Dawn: Gentle Accounts from Ordinary Patrol Deputies.

This book is a compilation of positive, uplifting stories of Police Officers going above and beyond to serve their communities. This book is being published to combat the negative news and social media stories that flood the internet.

The interior is currently being formatted but it looks as if the book will be around 162 pages.

Target Market(s)

This book is intended to target people who love law and order and who support police in America.

Industry/Entity Type

Book Publisher

Colors
000000
0456a4
33a6d7

Requirements
Must have
• I am not an artistic person so I don't have a solid idea of what the cover should look like. Here's what I'd like to see...

An American Flag (possible waving)
A police officer saluting or maybe the sillouhette of an officer on the cover (this is not a must but might look nice)
Possibly a police badge or a police patch
Possibly a police brevant or police car with red and blue lights activated
Possibly a police statue or picture of a police memorial

The color blue represents police officers so that is a must.

I would also like to have 'Foreword by Joy Tremwick' on the front cover.

Like I said above, I am not an artist so I will be relying heavily on opinions from the pros. I have the back of book blurb completed and can upload that when necessary.

Author name is Dustin Ferrow
Nice to have
• possibly a thin blue line symbol

This book is similar to the Warm Bread by the Window books. It's a bunch of feel good stories about American police officers. Anything I didn't mention that seems like a good idea is welcome.
Should not have
• Should not have anything negative toward police.

```html
<!DOCTYPE html>
<html lang="en">
<head>
<meta charset="utf-8">
<title>Steady Hands at Dawn — Cover</title>
<link rel="stylesheet" href="https://fonts.googleapis.com/css2?family=Bebas+Neue&display=swap">
<style>
  :root {
    --backdrop: #eeeeee;
    --flag-red: #c3343b;
    --flag-white: #f3efec;
    --flag-blue: #2d4f9e;
    --uniform-navy: #1c2c5e;
    --shadow-black: #050608;
    --author-blue: #1f4fae;
    --title-white: #ffffff;
  }
  html, body {
    margin: 0;
    padding: 0;
    width: 1200px;
    height: 537px;
    overflow: hidden;
    background: var(--backdrop);
  }
  .canvas {
    position: relative;
    width: 1200px;
    height: 537px;
  }
  .book-cover {
    position: absolute;
    left: 450px;
    top: 28px;
    width: 300px;
    height: 480px;
    overflow: hidden;
    font-family: "Bebas Neue", "Oswald", sans-serif;
    box-shadow: 0 1px 3px rgba(0,0,0,0.15);
  }
  .cover-art {
    position: absolute;
    inset: 0;
    width: 100%;
    height: 100%;
  }
  .author-name {
    position: absolute;
    top: 38px;
    left: 0;
    right: 0;
    text-align: center;
    padding-left: 30px;
    font-size: 15px;
    letter-spacing: 0.5px;
    color: var(--author-blue);
  }
  .title {
    position: absolute;
    top: 248px;
    left: 0;
    right: 0;
    margin: 0;
    text-align: center;
    font-weight: 400;
    font-size: 42px;
    line-height: 40px;
    letter-spacing: 1px;
    color: var(--title-white);
  }
  .subtitle {
    position: absolute;
    top: 355px;
    left: 0;
    right: 0;
    margin: 0;
    text-align: center;
    font-size: 15.5px;
    line-height: 16px;
    letter-spacing: 0.3px;
    color: var(--title-white);
  }
  .foreword {
    position: absolute;
    top: 438px;
    left: 0;
    right: 0;
    margin: 0;
    text-align: center;
    font-size: 15px;
    letter-spacing: 0.4px;
    color: var(--title-white);
  }
</style>
</head>
<body>
<main class="canvas">
  <section class="book-cover">
    <svg class="cover-art" viewBox="0 0 300 480" role="img" aria-label="Watercolor illustration of a waving American flag behind a uniformed police officer seen from the back">
      <defs>
        <linearGradient id="flagWash" x1="0" y1="0" x2="0.7" y2="1">
          <stop offset="0" stop-color="var(--flag-red)"/>
          <stop offset="0.18" stop-color="var(--flag-white)"/>
          <stop offset="0.34" stop-color="var(--flag-red)"/>
          <stop offset="0.5" stop-color="var(--flag-blue)"/>
          <stop offset="0.75" stop-color="var(--uniform-navy)"/>
          <stop offset="1" stop-color="var(--shadow-black)"/>
        </linearGradient>
      </defs>
      <rect width="300" height="480" fill="url(#flagWash)"/>
    </svg>
    <p class="author-name">Dustin Ferrow</p>
    <h1 class="title">Steady Hands<br>at Dawn:</h1>
    <p class="subtitle">Gentle Accounts from<br>Ordinary Patrol Deputies.</p>
    <p class="foreword">Foreword by Joy Tremwick</p>
  </section>
</main>
</body>
</html>
```